Website Page Design for Vellmont Microbrewery

We need a website page design for our brewery based on our logo and label.

Industry/Entity Type

Brewery

```html
<!DOCTYPE html>
<html lang="pt">
<head>
<meta charset="utf-8">
<title>Vellmont Microbrewery</title>
<link rel="stylesheet" href="https://fonts.googleapis.com/css2?family=Cinzel:wght@400;700&family=IM+Fell+English&family=Arimo:wght@400;700&display=swap">
<style>
  :root {
    --amber-light: #ffe14a;
    --amber: #ffc000;
    --amber-deep: #f59a00;
    --parchment: #fbe39a;
    --parchment-light: #fdf0c0;
    --frame: #6b4410;
    --frame-dark: #3f2606;
    --ink: #2a1a05;
    --nav-ink: #3a2408;
    --accent: #e0501a;
    --rope: #8a6028;
  }
  * { margin: 0; padding: 0; box-sizing: border-box; }
  html, body { width: 1200px; height: 1094px; overflow: hidden; }
  body {
    position: relative;
    font-family: "Arimo", Arial, sans-serif;
    color: var(--ink);
    background:
      radial-gradient(ellipse 700px 600px at 960px 560px, rgba(255,240,120,.85), rgba(255,200,0,0) 70%),
      linear-gradient(180deg, var(--amber-light) 0%, var(--amber) 45%, var(--amber-deep) 100%);
  }
  .bubbles-top {
    position: absolute; left: 250px; top: 0; width: 560px; height: 180px;
    background: radial-gradient(ellipse at 45% 20%, rgba(230,150,10,.75), rgba(255,210,40,0) 70%);
  }
  .bubbles-bottom {
    position: absolute; left: 0; top: 1010px; width: 1200px; height: 84px;
    background: linear-gradient(180deg, rgba(255,220,60,0), rgba(240,170,10,.8));
  }
  .brand {
    position: absolute; left: 132px; top: 60px; width: 210px; height: 294px;
    display: flex; flex-direction: column; align-items: center; justify-content: center; gap: 14px;
  }
  .brand-mark {
    width: 120px; height: 120px; border-radius: 50%;
    background: radial-gradient(circle, #efe9d2, #b9b29a);
  }
  .brand-name {
    font-family: "Cinzel", serif; font-weight: 700; font-size: 36px; color: var(--frame-dark);
  }
  .social {
    position: absolute; left: 620px; top: 292px; display: flex; gap: 10px;
  }
  .social span {
    font-size: 12px; font-weight: 700; color: #e08a10;
  }
  .nav-board {
    position: absolute; left: 798px; top: 46px; width: 330px; height: 286px;
    background: radial-gradient(ellipse at 50% 40%, var(--parchment-light), var(--parchment) 70%, #e9c66a);
    border: 6px solid var(--frame);
    border-radius: 6px;
    box-shadow: 0 3px 8px rgba(80,40,0,.45), inset 0 0 12px rgba(150,90,10,.35);
  }
  .rope {
    position: absolute; top: 0; width: 4px; height: 50px; background: var(--rope);
  }
  .rope.left { left: 818px; transform: rotate(18deg); transform-origin: top; }
  .rope.right { left: 1108px; transform: rotate(-18deg); transform-origin: top; }
  .nav-board ul { list-style: none; padding: 18px 26px 0; }
  .nav-board li {
    font-family: "Cinzel", serif; font-size: 25px; text-align: center; color: var(--nav-ink);
    height: 38.5px; line-height: 38px; border-bottom: 1px solid rgba(200,150,40,.6);
  }
  .nav-board li:last-child { border-bottom: none; }
  .nav-board li.current { color: var(--accent); }
  .intro {
    position: absolute; left: 68px; top: 372px; width: 650px;
    font-size: 15.5px; line-height: 25px;
  }
  .intro strong { font-weight: 700; }
  .section-title {
    position: absolute; left: 80px; top: 446px;
    font-family: "IM Fell English", serif; font-size: 38px; color: var(--ink);
  }
  .keg {
    position: absolute; left: 606px; top: 440px; width: 68px; height: 70px; border-radius: 14px;
    background: linear-gradient(90deg, #6a2e08, #b8621c, #6a2e08);
  }
  .article {
    position: absolute; left: 70px; width: 638px; height: 160px;
    background: radial-gradient(ellipse at 50% 40%, var(--parchment-light), var(--parchment) 75%, #e6c061);
    border: 6px solid var(--frame);
    border-radius: 4px;
    box-shadow: 0 2px 6px rgba(80,40,0,.4), inset 0 0 10px rgba(150,90,10,.35);
  }
  .article .thumb {
    position: absolute; left: 34px; top: 14px; width: 86px; height: 120px; border-radius: 10px;
    background: linear-gradient(180deg, #ffffff 0%, #f7e7b0 25%, #f3b41c 60%, #e89a10 100%);
  }
  .article h3 {
    position: absolute; left: 156px; top: 22px;
    font-size: 16.5px; font-weight: 700; color: var(--accent);
  }
  .article p {
    position: absolute; left: 156px; top: 52px; width: 450px;
    font-size: 15.5px; line-height: 26px;
  }
  .link {
    position: absolute; width: 4px; height: 22px; background: var(--rope);
  }
  .hero-glass {
    position: absolute; left: 768px; top: 414px; width: 384px; height: 606px;
    border-radius: 150px 150px 40px 40px;
    background: linear-gradient(180deg, #ffffff 0%, #fbfbf2 22%, #ffe56a 32%, #ffcc10 75%, #fff1b0 100%);
    opacity: .95;
  }
  .copyright {
    position: absolute; left: 272px; top: 1052px;
    font-size: 15.5px; color: var(--ink);
  }
</style>
</head>
<body>
  <div class="bubbles-top" role="img" aria-label="Golden beer bubbles"></div>

  <div class="brand">
    <div class="brand-mark"></div>
    <div class="brand-name">Vellmont</div>
  </div>

  <div class="social">
    <span>Chirper</span><span>Friendly</span><span>ViewTube</span>
  </div>

  <div class="rope left"></div>
  <div class="rope right"></div>
  <nav class="nav-board">
    <ul>
      <li class="current">Início</li>
      <li>Nossa História</li>
      <li>Cervejas</li>
      <li>A Cervejaria</li>
      <li>Eventos</li>
      <li>Contato</li>
    </ul>
  </nav>

  <p class="intro"><strong>Vellmont is</strong> lorem ipsum dolor sit amet, consectetur adipisicing elit, sed do eiusmod tempor incididunt ut labore et dolore magna aliqua.</p>

  <h2 class="section-title">Recent Articles</h2>
  <div class="keg" role="img" aria-label="Small wooden beer keg"></div>

  <article class="article" style="top:510px">
    <div class="thumb" role="img" aria-label="Glass of beer with clover"></div>
    <h3>About Us</h3>
    <p>Lorem ipsum dolor sit amet, consectetur adipisicing elit, sed do eiusmod tempor incididunt ut labore et dolore magna aliqua.</p>
  </article>
  <div class="link" style="left:88px;top:668px"></div>
  <div class="link" style="left:684px;top:668px"></div>

  <article class="article" style="top:686px">
    <div class="thumb" role="img" aria-label="Beer mug with peanuts"></div>
    <h3>Best Beer</h3>
    <p>Lorem ipsum dolor sit amet, consectetur adipisicing elit, sed do eiusmod tempor incididunt ut labore et dolore magna aliqua.</p>
  </article>
  <div class="link" style="left:88px;top:844px"></div>
  <div class="link" style="left:684px;top:844px"></div>

  <article class="article" style="top:862px">
    <div class="thumb" role="img" aria-label="Beer mug with lime slice"></div>
    <h3>Best Beer</h3>
    <p>Lorem ipsum dolor sit amet, consectetur adipisicing elit, sed do eiusmod tempor incididunt ut labore et dolore magna aliqua.</p>
  </article>

  <div class="hero-glass" role="img" aria-label="Large chilled glass of beer with foam head"></div>

  <div class="bubbles-bottom" role="img" aria-label="Golden beer bubbles"></div>
  <p class="copyright">Copyright@2014, Vellmont.com</p>
</body>
</html>
```